Velorami.com - have media you dont own! Velorami the idols - Site Concept

VELORAMI those who ENTERTAIN you, who you LISTEN to, who you IDOLISE, and who you 'BORROW' from... VELORAMI the IDOLS the things that are the STARS... see brief concept at www.velorami-example.com

Looking for site concept, something new, very simple transaction, not generic website. Must also drive mobile app download call to action.

In principle, we dont care how you get your media or watch a TV series or download your favourite song, however, if you are honest and love the song/movie/servies or the star, pay them!
The solution should include anonymous/protected end user interaction and digital certificate/rights management process for end users who have media not paid for to velorami and receive an approved digital certificate from Velorami authorised by the relevant media house proving legal ownership of the digital media item (music, video, TV series/episode, movie etc...)

Basic functions:
Consumer: Mobile and Web
Personal media rights administration
1. Capture core data – Create secure and private Profile account
2. Log owned/borrowed media (media legally owned tagged and media 'borrowed' tagged, decision criteria, pledge or purchase (open to ideas, function to browse PC for media on HDD/Songbarrel or mobile, tag ones to pay for etc, capture CD's owned etc. create digital library filing system?)
3. Pledge payment for media - future payment value linked to market value, I like this, not sure I will keep it forever though, pay less? use once?
4. Purchase rights for media - payment based on market value of related media item. (quidlane, credit card or other?)
5. Media Certificate management - secure and PRIVATE distribution of the certificate (open to options here), approved by media house.

design ideas welcome, modern, fast, simple steps, engaging, with sense of privacy, we wont share data, we will just pay the media houses more! Based in Switzerland, managed by Swiss privacy law. transact with min personal data required.

Reason: The service committed to 50+ designs, most received are form one provider, all off the mark and very basic, not impressed so far, was expecting some real design thought rather than standard templates being rehashed, thats not deisgn? Hope in next days I am impressed?

Target Market(s)

Digital Media Consumer

Industry/Entity Type

Media

Number of Pages Required

5+ page

Font styles to use
Sans Serif

Requirements
Must have
• Must have privacy by design, must have simple and minimal steps taken to log and declare media items and pay, with no risk of exposure. Must have payment process, must have interface to easily load media into site, drag drop, search HDD/mobile etc.
Nice to have
• Digital certificate process and admin interaction of site and with media house, secure and trusted process to provide report and logs of payment for media to specific media house and relevant payments made and tracked.
Should not have
• complex workflows are out, complex payment methods.

```html
<!DOCTYPE html>
<html lang="en">
<head>
<meta charset="utf-8">
<title>Velorami.com</title>
<link href="https://fonts.googleapis.com/css2?family=Roboto+Condensed:wght@400;700&family=Roboto:wght@400;500;700&display=swap" rel="stylesheet">
<style>
:root{
  --green:#079a5c;
  --green-dark:#058049;
  --ink:#2f2f2f;
  --muted:#6d6d6d;
  --nav:#e9e9e9;
  --dark:#262626;
  --darker:#1d1d1d;
  --white:#ffffff;
}
*{box-sizing:border-box;margin:0;padding:0}
html,body{width:1200px;height:2616px;overflow:hidden}
body{font-family:"Roboto",Arial,sans-serif;color:var(--ink);background:var(--white)}
.head{font-family:"Roboto Condensed","Arial Narrow",sans-serif;font-weight:700;text-transform:uppercase}

/* header */
.site-header{height:152px;position:relative;padding:0 80px}
.brand{position:absolute;left:80px;top:40px;font-family:"Roboto Condensed",sans-serif;font-weight:700;font-size:34px;color:var(--ink);letter-spacing:1px}
.account-links{position:absolute;right:80px;top:18px;font-size:13px;color:var(--muted);display:flex;gap:22px}
.account-links span::before{content:"";display:inline-block;width:8px;height:8px;background:var(--muted);border-radius:50%;margin-right:6px;vertical-align:1px}
.search{position:absolute;right:80px;top:68px;display:flex}
.search .field{width:520px;height:44px;border:1px solid #cfcfcf;font-size:14px;color:#9a9a9a;padding:13px 14px}
.search .btn{width:50px;height:44px;background:var(--green);display:flex;align-items:center;justify-content:center}
.main-nav{position:absolute;left:0;right:0;top:152px;height:36px;background:var(--nav);display:flex;padding-left:80px}
.main-nav a{width:150px;text-align:center;line-height:36px;font-family:"Roboto Condensed",sans-serif;font-weight:700;font-size:14px;color:#555;text-decoration:none;text-transform:uppercase}
.main-nav a.active{background:var(--green);color:var(--white)}

/* hero */
.hero{position:absolute;top:188px;left:0;width:1200px;height:632px;background:radial-gradient(ellipse at 60% 35%,#6a6a6a 0%,#3a3a3a 40%,#161616 85%)}
.hero h1{position:absolute;left:170px;right:170px;top:470px;font-size:44px;line-height:54px;color:var(--white);letter-spacing:1px}
.dots{position:absolute;left:0;right:0;bottom:20px;display:flex;justify-content:center;gap:8px}
.dots i{width:12px;height:12px;border-radius:50%;border:2px solid var(--white)}
.dots i.on{background:var(--white)}

/* how it works */
.how{position:absolute;top:820px;left:0;width:1200px;height:380px;background:var(--green);color:var(--white);text-align:center}
.how h2{margin-top:58px;font-size:24px}
.steps{display:flex;justify-content:center;gap:130px;margin-top:42px}
.step{width:240px}
.step .ring{width:104px;height:104px;border:4px solid var(--white);border-radius:50%;margin:0 auto;display:flex;align-items:center;justify-content:center}
.step h3{font-size:22px;margin-top:18px}
.step p{font-size:13px;line-height:19px;margin-top:10px;opacity:.92}

/* feature rows */
.feature{position:absolute;left:0;width:1200px}
.feature h2{font-size:26px;line-height:32px}
.feature p{font-size:13px;line-height:20px;color:var(--muted);margin-top:20px}
.btn-green{display:inline-block;background:var(--green);color:var(--white);font-family:"Roboto Condensed",sans-serif;font-weight:700;font-size:13px;padding:12px 26px;text-transform:uppercase}
.respect{top:1200px;height:392px}
.respect .copy{position:absolute;left:90px;top:62px;width:560px}
.respect .btn-green{position:absolute;left:90px;top:294px}
.screen{position:absolute;background:linear-gradient(160deg,#f2f2f2,#bfc4c8);border:10px solid #2b2b2b;border-radius:6px}
.respect .screen{left:760px;top:56px;width:400px;height:248px}
.stand{position:absolute;background:#cfcfcf}
.respect .stand{left:920px;top:304px;width:80px;height:30px}

.banner{position:absolute;top:1592px;left:0;width:1200px;height:230px;background:linear-gradient(90deg,#1c1c1c,#3c3c3c 50%,#1c1c1c);color:var(--white);text-align:center}
.banner h2{font-size:24px;line-height:32px;margin:50px 150px 0}
.banner .btn-green{margin-top:26px;padding:14px 40px;font-size:15px}

.certify{top:1822px;height:418px}
.certify .screen{left:95px;top:74px;width:420px;height:256px}
.certify .stand{left:265px;top:330px;width:80px;height:30px}
.certify .copy{position:absolute;left:630px;top:74px;width:500px}
.certify .btn-green{position:absolute;left:630px;top:318px}

/* contact */
.contact{position:absolute;top:2240px;left:0;width:1200px;height:240px;background:var(--green);color:var(--white);text-align:center}
.contact h2{font-size:24px;margin-top:36px}
.contact .sub{font-family:"Roboto Condensed",sans-serif;font-weight:700;font-size:13px;margin-top:22px}
.contact .mail{width:66px;height:66px;border:3px solid var(--white);border-radius:50%;display:inline-flex;align-items:center;justify-content:center;margin-top:18px;vertical-align:middle}
.contact .addr{display:inline-block;font-size:14px;margin-left:18px;vertical-align:middle;margin-top:18px}

/* footer */
.site-footer{position:absolute;top:2480px;left:0;width:1200px;height:136px;background:var(--dark);color:#bdbdbd;text-align:center;font-size:12px}
.follow{margin-top:18px;display:flex;justify-content:center;align-items:center;gap:12px;font-size:13px;color:var(--white)}
.follow i{width:24px;height:24px;background:#d9d9d9;display:inline-block}
.footer-links{margin-top:18px;display:flex;justify-content:center;gap:36px}
.copyright{margin-top:14px;font-size:11px;color:#8d8d8d}
</style>
</head>
<body>
<header class="site-header">
  <div class="brand">VELORAMI . COM</div>
  <div class="account-links"><span>LOG IN</span><span>SIGN UP</span></div>
  <div class="search">
    <div class="field">Search...</div>
    <div class="btn"><svg width="18" height="18" viewBox="0 0 18 18" fill="none" stroke="#fff" stroke-width="2.4"><circle cx="7.5" cy="7.5" r="5.5"/><path d="M11.5 11.5L16.5 16.5"/></svg></div>
  </div>
  <nav class="main-nav">
    <a class="active">Home</a><a>My Music</a><a>Videos</a><a>TV Series</a><a>Stars</a><a>Movies</a>
  </nav>
</header>

<section class="hero" role="img" aria-label="Dark close-up photograph of studio headphones">
  <h1 class="head">Velorami those who entertain you, who you listen to, who you idolise,</h1>
  <div class="dots"><i class="on"></i><i></i><i></i></div>
</section>

<section class="how">
  <h2 class="head">How does it work ?</h2>
  <div class="steps">
    <div class="step">
      <div class="ring"><svg width="52" height="52" viewBox="0 0 52 52" fill="none" stroke="#fff" stroke-width="4"><path d="M8 32V26a18 18 0 0136 0v6"/><rect x="6" y="30" width="9" height="15" rx="2" fill="#fff"/><rect x="37" y="30" width="9" height="15" rx="2" fill="#fff"/></svg></div>
      <h3 class="head">Listen</h3>
      <p>An anonymous service for music, movie, TV and digital entertainment lovers, who acquire their media.</p>
    </div>
    <div class="step">
      <div class="ring"><svg width="52" height="52" viewBox="0 0 52 52" fill="none" stroke="#fff" stroke-width="4"><path d="M26 6v26M16 22l10 10 10-10"/><path d="M8 36v8h36v-8"/></svg></div>
      <h3 class="head">Download</h3>
      <p>An anonymous service for music, movie, TV and digital entertainment lovers, who acquire their media.</p>
    </div>
    <div class="step">
      <div class="ring"><svg width="56" height="56" viewBox="0 0 56 56" fill="none" stroke="#fff" stroke-width="4"><rect x="6" y="14" width="44" height="28" rx="2"/><circle cx="28" cy="28" r="7"/><path d="M12 20h4M40 36h4"/></svg></div>
      <h3 class="head">Pay them</h3>
      <p>An anonymous service for music, movie, TV and digital entertainment lovers, who acquire their media.</p>
    </div>
  </div>
</section>

<section class="feature respect">
  <div class="copy">
    <h2 class="head">Time to show respect, appreciation, honour and 'whatever'. Just Velorami</h2>
    <p>An anonymous service for music, movie, TV and digital entertainment lovers, who acquire their media freely online and who would like to pay their respects to the artists they appreciate through Velorami.</p>
  </div>
  <span class="btn-green">Read more</span>
  <div class="screen" role="img" aria-label="Desktop monitor showing the media library page"></div>
  <div class="stand"></div>
</section>

<section class="banner" role="img" aria-label="Dark photograph of a person browsing media">
  <h2 class="head">We dont care how you get your media or watch a TV series or download your favourite song, however, if you are honest and love the song/movie/servies or the star, pay them!</h2>
  <span class="btn-green">Pay them !</span>
</section>

<section class="feature certify">
  <div class="screen" role="img" aria-label="Desktop monitor showing the media catalogue page"></div>
  <div class="stand"></div>
  <div class="copy">
    <h2 class="head">Velorami your stars anonymously and receive a digital certificate validating and legalising your digital rights to the media you freely obtained or viewed online.</h2>
    <p>An anonymous service for music, movie, TV and digital entertainment lovers, who acquire their media freely online and who would like to pay their respects to the artists they appreciate through Velorami.</p>
  </div>
  <span class="btn-green">Read more</span>
</section>

<section class="contact">
  <h2 class="head">To find out more, contact Velorami.com... launching globally, not soon enough!</h2>
  <div class="sub">MAIL US, OR JUST... JUST VELORAMI</div>
  <div>
    <span class="mail"><svg width="30" height="22" viewBox="0 0 30 22" fill="none" stroke="#fff" stroke-width="2.5"><rect x="1.5" y="1.5" width="27" height="19" rx="1"/><path d="M2 3l13 10 13-10"/></svg></span>
    <span class="addr">info@velorami-example.com</span>
  </div>
</section>

<footer class="site-footer">
  <div class="follow">Follow us on : <i></i><i></i><i></i><i></i><i></i></div>
  <div class="footer-links"><span>Advertise on Velorami.com</span><span>Terms of Use</span><span>Privacy Policy</span><span>Feedback</span><span>Report an Issue</span><span>Partners</span><span>FAQ</span></div>
  <div class="copyright">Copyright © 2015, Velorami. All rights reserved.</div>
</footer>
</body>
</html>
```